Bag packaging design of sliced bread

The project is for design of line of sliced bread with different flavours. The brand of the bread will be "Velorasa". The shape of the bread will be oval. The bread will be packed in a bag. I attach the layout of the bag. The bag will be closed with a plastic clip. I attach images of similar products. The idea is to have one main design and then each colour to be different type of bread like those in the images 2 and 5.

```html
<!DOCTYPE html>
<html lang="en">
<head>
<meta charset="utf-8">
<title>Velorasa Sliced Bread – Bag Design</title>
<link rel="stylesheet" href="https://fonts.googleapis.com/css2?family=Alfa+Slab+One&family=Montserrat:wght@500;700&family=Oswald:wght@500&family=Dancing+Script:wght@700&family=Pinyon+Script&display=swap">
<style>
  :root {
    --backdrop: #e2b22c;
    --leaf: #86bd3a;
    --leaf-dark: #74a82c;
    --paper: #ffffff;
    --crust: #8a4713;
    --crust-dark: #4a2410;
    --crumb-light: #e9c79a;
    --crumb-mid: #d6a873;
    --sketch: #e4e4e4;
  }
  * { margin: 0; padding: 0; box-sizing: border-box; }
  html, body { width: 1041px; height: 1200px; overflow: hidden; }
  body {
    background: var(--backdrop);
    position: relative;
    font-family: "Montserrat", sans-serif;
  }
  .bag { position: absolute; left: 0; top: 0; width: 1041px; height: 1200px; }

  .bag-neck { position: absolute; left: 372px; top: 73px; width: 293px; height: 200px; }
  .neck-band {
    position: absolute; left: 372px; top: 81px; width: 293px; height: 30px;
    background: var(--paper);
    display: flex; align-items: center; justify-content: center; gap: 22px;
    color: var(--leaf-dark); font-size: 17px; font-weight: 700; overflow: hidden; white-space: nowrap;
  }
  .neck-band .dot { width: 8px; height: 8px; background: var(--leaf-dark); border-radius: 50%; }
  .neck-emblem {
    position: absolute; left: 456px; top: 131px; width: 125px; height: 119px;
    background: radial-gradient(ellipse at center, rgba(255,255,255,.85), rgba(255,255,255,.15) 70%);
    border-radius: 50% 50% 10px 10px;
  }

  .bag-body {
    position: absolute; left: 308px; top: 267px; width: 424px; height: 872px;
    border-radius: 130px / 170px; overflow: hidden; background: var(--leaf);
  }
  .brand-panel { position: absolute; left: 0; top: 0; width: 100%; height: 163px; text-align: center; }
  .brand-name {
    position: absolute; top: 36px; width: 100%;
    font-family: "Montserrat", sans-serif; font-weight: 700; font-size: 56px;
    color: var(--paper); letter-spacing: 1px;
  }
  .brand-rule { position: absolute; left: 96px; right: 96px; top: 118px; height: 1px; background: var(--paper); }
  .brand-tagline {
    position: absolute; top: 124px; width: 100%;
    font-size: 19px; font-weight: 500; color: var(--paper); letter-spacing: .5px;
  }

  .hero-panel { position: absolute; left: 0; top: 163px; width: 100%; height: 293px; background: var(--paper); text-align: center; }
  .field-sketch {
    position: absolute; left: 0; bottom: 0; width: 100%; height: 120px;
    background: linear-gradient(to bottom, rgba(228,228,228,0), var(--sketch));
  }
  .wheat-left, .wheat-right {
    position: absolute; top: 40px; width: 50px; height: 130px;
    background: linear-gradient(to bottom, #f0c86a, #e3a43a); opacity: .55; border-radius: 40px;
  }
  .wheat-left { left: 8px; } .wheat-right { right: 8px; }
  .product-name {
    position: absolute; top: 24px; width: 100%;
    font-family: "Alfa Slab One", serif; font-size: 86px; line-height: 1; color: var(--crust);
    letter-spacing: 1px;
  }
  .ribbon { position: absolute; left: 49px; top: 119px; width: 314px; height: 52px; }
  .ribbon-text {
    position: absolute; left: 49px; top: 119px; width: 314px; height: 52px; line-height: 52px;
    font-size: 23px; font-weight: 500; color: var(--paper); letter-spacing: .5px;
  }
  .ribbon-text b { font-weight: 700; }
  .benefit {
    position: absolute; top: 178px; width: 100%;
    font-family: "Oswald", sans-serif; font-size: 23px; color: var(--crust); letter-spacing: .5px;
  }
  .natural {
    position: absolute; top: 222px; width: 100%;
    font-family: "Dancing Script", cursive; font-size: 40px; color: var(--crust-dark);
  }

  .window {
    position: absolute; left: 0; top: 456px; width: 100%; height: 230px;
    background: linear-gradient(100deg, var(--crumb-mid), var(--crumb-light) 55%, var(--crumb-mid));
  }
  .weight-cap {
    position: absolute; left: 0; top: 456px; width: 100%; height: 44px;
    background: var(--leaf); border-radius: 0 0 50% 50% / 0 0 100% 100%;
    text-align: center; line-height: 40px;
    font-family: "Oswald", sans-serif; font-size: 21px; color: var(--paper); letter-spacing: 1px;
  }
  .weight-cap b { font-weight: 500; }

  .claims-panel { position: absolute; left: 0; top: 674px; width: 100%; height: 198px; background: var(--leaf); text-align: center; color: var(--paper); }
  .slogan { position: absolute; top: 20px; width: 100%; font-family: "Pinyon Script", cursive; font-size: 29px; line-height: 26px; }
  .claims-rule { position: absolute; left: 80px; right: 80px; height: 1px; background: var(--paper); }
  .claims-rule.top { top: 79px; } .claims-rule.bottom { top: 102px; }
  .claim { position: absolute; top: 82px; width: 100%; font-family: "Oswald", sans-serif; font-size: 15px; letter-spacing: .4px; }
  .badges { position: absolute; top: 113px; left: 0; width: 100%; display: flex; justify-content: center; gap: 13px; }
  .badge { width: 44px; height: 46px; border: 2px solid var(--paper); border-radius: 18px 18px 6px 6px;
    display: flex; flex-direction: column; align-items: center; justify-content: flex-end; padding-bottom: 4px; }
  .badge svg { width: 18px; height: 18px; margin-bottom: 3px; }
  .badge span { font-family: "Oswald", sans-serif; font-size: 6px; line-height: 1; }
</style>
</head>
<body>
<div class="bag">
  <svg class="bag-neck" viewBox="0 0 293 200" aria-hidden="true">
    <path d="M0 10 Q146 0 293 10 L280 60 Q240 150 180 190 L175 200 L118 200 L113 190 Q53 150 13 60 Z" fill="#86bd3a"/>
  </svg>
  <div class="neck-band"><span>Velorasa</span><span class="dot"></span><span>Velorasa</span><span class="dot"></span><span>Velorasa</span></div>
  <div class="neck-emblem" role="img" aria-label="White wheat ears rising from a hill"></div>

  <div class="bag-body">
    <section class="brand-panel">
      <div class="brand-name">Velorasa</div>
      <div class="brand-rule"></div>
      <div class="brand-tagline">LOVE WHAT YOU EAT</div>
    </section>

    <section class="hero-panel">
      <div class="field-sketch" role="img" aria-label="Sketch of a wheat field with a windmill"></div>
      <div class="wheat-left" role="img" aria-label="Golden wheat ear"></div>
      <div class="wheat-right" role="img" aria-label="Golden wheat ear"></div>
      <h1 class="product-name">BREAD</h1>
      <svg class="ribbon" viewBox="0 0 314 52" aria-hidden="true">
        <path d="M0 0 H314 L302 26 L314 52 H0 L12 26 Z" fill="#4a2410"/>
        <line x1="14" y1="6" x2="300" y2="6" stroke="#fff" stroke-width="2" stroke-dasharray="1 4"/>
        <line x1="14" y1="46" x2="300" y2="46" stroke="#fff" stroke-width="2" stroke-dasharray="1 4"/>
      </svg>
      <div class="ribbon-text">NOW YOU CAN <b>EAT</b></div>
      <div class="benefit">- FRESH NUTRITION BREAD -</div>
      <div class="natural">100% Natural</div>
    </section>

    <div class="window" role="img" aria-label="Clear window showing the bread slices"></div>
    <div class="weight-cap">- Net Wt. <b>510g</b> -</div>

    <section class="claims-panel">
      <p class="slogan">Bread that you and<br>your family will love</p>
      <div class="claims-rule top"></div>
      <div class="claim">NO ARTIFICIAL FLAVORS AND COLORS</div>
      <div class="claims-rule bottom"></div>
      <div class="badges">
        <div class="badge"><svg viewBox="0 0 18 18"><path d="M9 2v12M4 9l5 5 5-5" stroke="#fff" stroke-width="2" fill="none"/></svg><span>LOW SUGAR</span></div>
        <div class="badge"><svg viewBox="0 0 18 18"><path d="M9 2v12M4 9l5 5 5-5" stroke="#fff" stroke-width="2" fill="none"/></svg><span>LOW SODIUM</span></div>
        <div class="badge"><svg viewBox="0 0 18 18"><path d="M9 16V4M4 9l5-5 5 5" stroke="#fff" stroke-width="2" fill="none"/></svg><span>HIGH FIBER</span></div>
        <div class="badge"><svg viewBox="0 0 18 18"><path d="M9 16V4M4 9l5-5 5 5" stroke="#fff" stroke-width="2" fill="none"/></svg><span>HIGH PROTEIN</span></div>
      </div>
    </section>
  </div>
</div>
</body>
</html>
```